Church needs a street sign design

We're a small church located in Silicon Valley, California. Our website is https://www.hfbmerrow.org/ and our address is 4817 Larkfield Ave, San Jose, California, 95873. You can look up our location on Google Maps to see the sign from Street View. I have uploaded an image of the street sign as well. The marquee, the top section of the sign, and the separating line between them both will be removed. We're seeking a design for a new backlit acrylic insert that will go on the front of the light box and the back of the lightbox. The acrylic sign will fill the entire external frame. In the future, we may build a decorative wood frame around the structural legs, as visualized in one of the uploaded files. The church's brand colors are: #003366 (dark blue), #ff6600 (vibrant orange), #228b22 (forest green). I have also uploaded the church's logo assets. Our primary font is Montserrat and the secondary is Poppins. You can deviate from these colors/fonts if the sign is still coherent with the rest of our branding. Our branding values are mission, truth, passion, and community (please do not put those words on the sign! They are just intended to guide the look of the design). The sign dimensions are 96" by 47.5". Keep in mind that the sign will be backlit on a busy street side. It will also be positioned next to an old-looking church building. We do NOT want a sign that looks traditional, old, or antiquated. Instead, we want a modern-looking sign that pairs well with our old building while helping it look more modern too. We would also like the web address clearly visible on the sign: hfbmerrow.org. If you have any questions, just let me know!

```html
<!DOCTYPE html>
<html lang="en">
<head>
<meta charset="utf-8">
<title>Harbor Fellowship Bible – Street Sign</title>
<link rel="stylesheet" href="https://fonts.googleapis.com/css2?family=Montserrat:wght@600&family=Poppins:wght@600;700&display=swap">
<style>
  :root {
    --page-bg: #b4bac6;
    --sky-deep: #003366;
    --sky-mid: #0b4f86;
    --sky-light: #0a6a9c;
    --band-orange: #ff6a00;
    --band-red: #ff1e00;
    --ink-white: #ffffff;
    --pin-blue: #0d3468;
  }
  * { margin: 0; padding: 0; box-sizing: border-box; }
  html, body {
    width: 762px;
    height: 1200px;
    overflow: hidden;
    background: var(--page-bg);
  }
  .canvas {
    position: relative;
    width: 762px;
    height: 1200px;
  }
  .street-sign {
    position: absolute;
    left: 31px;
    top: 428px;
    width: 700px;
    height: 344px;
    box-shadow: 0 8px 14px rgba(0, 0, 0, 0.35);
  }
  .street-sign svg { display: block; width: 100%; height: 100%; }
  .name-main { font-family: "Montserrat", sans-serif; font-weight: 600; fill: var(--ink-white); }
  .name-sub { font-family: "Montserrat", sans-serif; font-weight: 600; fill: var(--ink-white); }
  .location-title { font-family: "Poppins", sans-serif; font-weight: 700; fill: var(--ink-white); }
  .location-address { font-family: "Poppins", sans-serif; font-weight: 600; fill: var(--ink-white); }
  .web-address { font-family: "Poppins", sans-serif; font-weight: 700; fill: var(--ink-white); }
  .brand-mark { fill: none; stroke: var(--ink-white); stroke-width: 13; }
  .pin-icon { fill: var(--pin-blue); }
  .pin-dot { fill: var(--band-orange); }
</style>
</head>
<body>
<main class="canvas">
  <section class="street-sign" aria-label="Harbor Fellowship Bible street sign">
    <svg viewBox="0 0 700 344" xmlns="http://www.w3.org/2000/svg">
      <defs>
        <linearGradient id="sky-fill" x1="0" y1="0" x2="0.3" y2="1">
          <stop offset="0" stop-color="var(--sky-deep)"/>
          <stop offset="0.55" stop-color="var(--sky-mid)"/>
          <stop offset="1" stop-color="var(--sky-light)"/>
        </linearGradient>
        <linearGradient id="band-fill" x1="0" y1="1" x2="1" y2="0">
          <stop offset="0" stop-color="var(--band-orange)"/>
          <stop offset="0.6" stop-color="#ff4a00"/>
          <stop offset="1" stop-color="var(--band-red)"/>
        </linearGradient>
      </defs>

      <rect class="sky-backdrop" role="img" aria-label="Blue cloudy sky photograph" x="0" y="0" width="700" height="344" fill="url(#sky-fill)"/>

      <path class="info-band" role="img" aria-label="Orange sunset clouds photograph"
            d="M56 170 H700 V316 H56 A22 22 0 0 1 34 294 V192 A22 22 0 0 1 56 170 Z" fill="url(#band-fill)"/>

      <rect class="brand-mark" x="62" y="36" width="128" height="128"/>

      <text class="name-main" x="224" y="124" font-size="110" textLength="429" lengthAdjust="spacingAndGlyphs">HARBOR</text>
      <text class="name-sub" x="226" y="151" font-size="37" textLength="421" lengthAdjust="spacingAndGlyphs">FELLOWSHIP BIBLE</text>

      <g class="pin-icon-group">
        <path class="pin-icon" d="M195 196 a15.5 15.5 0 0 1 15.5 15.5 c0 10 -15.5 30.5 -15.5 30.5 c0 0 -15.5 -20.5 -15.5 -30.5 a15.5 15.5 0 0 1 15.5 -15.5 Z"/>
        <circle class="pin-dot" cx="195" cy="211" r="7"/>
      </g>

      <text class="location-title" x="216" y="217" font-size="29" textLength="436" lengthAdjust="spacingAndGlyphs">SILICON VALLEY, CALIFORNIA</text>
      <text class="location-address" x="219" y="242" font-size="19" textLength="427" lengthAdjust="spacingAndGlyphs">4817 Larkfield Ave, San Jose, California, 95873</text>
      <text class="web-address" x="179" y="294" font-size="50" textLength="480" lengthAdjust="spacingAndGlyphs">www.hfbmerrow.org</text>
    </svg>
  </section>
</main>
</body>
</html>
```